Business card design incorporating discount offer

We are a trade services company and we need a double sided business card that is going to be used by our tradesmen to give to customers on completion of their jobs.

Below are the key elements of the card that we would like to include:

-Main logo with text 'Expert Property Care' underneath.
-Up to 12 smaller icon logos with text 'Your local all-trade experts' to emphasise the point that we cover all the trades
-Discount offer - 10% discount
-Telephone number and website address
-Blank space for tradesman to enter his/her name
-Request for customer feedback with feedback url

This business card will be printed on regular card. In the past we have favoured designs that use a black background but we're open to new ideas.

I have attached a few files:

-A simple wire frame example to show how this card could look with the different elements mentioned above, feel free to use a layout similar to this or come up with something totally different (biz-card.pdf)
-Front and back of a loyalty card the we've used in the past (this card was printed on plastic)
-Front and back of a key fob design that we've previously used (this card was printed on plastic)
-A logo file with the 12 small icons and the main logo image

If you need further images or information please ask.

```html
<!DOCTYPE html>
<html lang="en">
<head>
<meta charset="utf-8">
<title>HDK Expert Property Care – Business Card</title>
<link rel="stylesheet" href="https://fonts.googleapis.com/css2?family=Arimo:wght@400;700&family=Ubuntu:wght@400&display=swap">
<style>
  :root {
    --backdrop: #e4e1dc;
    --card-black: #0d0d0d;
    --card-shade: #1c1c1c;
    --white: #ffffff;
    --offer-red: #e4202a;
    --brand-blue: #1ba7e0;
    --link-orange: #f7941d;
    --ink: #111111;
  }
  * { box-sizing: border-box; margin: 0; padding: 0; }
  html, body { width: 1200px; height: 1200px; overflow: hidden; }
  body {
    background: var(--backdrop);
    font-family: "Arimo", Arial, sans-serif;
    position: relative;
  }
  .card {
    position: absolute;
    left: 180px;
    width: 840px;
    height: 550px;
    background: var(--card-black);
    overflow: hidden;
    box-shadow: 0 6px 18px rgba(0,0,0,0.25);
  }
  .card--front { top: 30px; }
  .card--back { top: 620px; }
  .card__art { position: absolute; inset: 0; width: 100%; height: 100%; }
  .abs { position: absolute; white-space: nowrap; }

  /* Front */
  .brand { left: 60px; top: 118px; display: flex; align-items: center; gap: 22px; }
  .brand__dot { width: 84px; height: 84px; border-radius: 50%; background: var(--brand-blue); }
  .brand__name { font-weight: 700; font-size: 104px; line-height: 1; color: var(--white); letter-spacing: 2px; }
  .tagline { left: 58px; top: 268px; font-weight: 700; font-size: 35px; color: var(--white); }
  .contact { left: 62px; display: flex; align-items: center; gap: 16px; font-size: 28px; }
  .contact--phone { top: 424px; color: var(--white); }
  .contact--web { top: 466px; color: var(--link-orange); font-weight: 700; }
  .contact svg { width: 26px; height: 26px; }

  .offer { left: 520px; width: 300px; text-align: center; top: 100px; }
  .offer__amount { font-weight: 700; font-size: 132px; line-height: 1; color: var(--offer-red); letter-spacing: -2px; }
  .offer__label { font-weight: 700; font-size: 50px; line-height: 1; color: var(--ink); margin-top: 6px; }
  .offer__note { font-size: 22px; color: var(--ink); margin-top: 4px; }
  .offer-terms { left: 520px; width: 300px; top: 444px; text-align: center; font-size: 20px; line-height: 1.45; color: var(--ink); white-space: normal; }

  /* Back */
  .trade-icons {
    position: absolute; left: 32px; top: 30px;
    display: grid; grid-template-columns: 74px 74px; column-gap: 14px; row-gap: 11px;
  }
  .trade-icon { width: 74px; height: 74px; border-radius: 12px; border: 2px solid rgba(255,255,255,0.35); }
  .headline { left: 230px; top: 52px; font-family: "Ubuntu", Arial, sans-serif; font-size: 44px; color: var(--white); }
  .headline-rule { position: absolute; left: 230px; top: 118px; width: 576px; height: 3px; background: var(--white); }
  .field-label { left: 232px; top: 162px; font-size: 20px; color: var(--white); letter-spacing: 0.5px; }
  .name-field { position: absolute; left: 232px; top: 205px; width: 572px; height: 58px; background: var(--white); }
  .feedback { left: 230px; width: 576px; top: 318px; text-align: center; color: var(--white); }
  .feedback__question { font-size: 31px; font-weight: 700; }
  .feedback__ask { font-size: 24px; margin-top: 10px; }
  .feedback__url { font-size: 31px; margin-top: 8px; }
  .feedback__stars { font-size: 28px; letter-spacing: 3px; margin-top: 8px; }
</style>
</head>
<body>

<section class="card card--front" aria-label="Business card front">
  <svg class="card__art" viewBox="0 0 840 550" preserveAspectRatio="none" aria-hidden="true">
    <path d="M0 550 C 140 420, 330 360, 480 430 L 470 550 Z" fill="var(--card-shade)"/>
    <path d="M580 0 C 540 40, 500 150, 530 260 C 560 380, 520 480, 470 550 L 840 550 L 840 0 Z" fill="var(--white)"/>
    <path d="M580 0 C 540 40, 500 150, 530 260 C 560 380, 520 480, 470 550" fill="none" stroke="var(--offer-red)" stroke-width="6"/>
  </svg>

  <div class="abs brand">
    <span class="brand__dot"></span>
    <span class="brand__name">HDK</span>
  </div>
  <div class="abs tagline">Expert Property Care</div>

  <div class="abs contact contact--phone">
    <svg viewBox="0 0 24 24" aria-hidden="true"><path fill="var(--brand-blue)" d="M3 8c0-2 3-4 9-4s9 2 9 4v2h-5V8c-1-.5-2.5-.7-4-.7S9 7.5 8 8v2H3zM6 12h12l2 7H4z"/><circle cx="12" cy="15.5" r="2" fill="var(--card-black)"/></svg>
    <span>0800 555 0142</span>
  </div>
  <div class="abs contact contact--web">
    <svg viewBox="0 0 24 24" aria-hidden="true"><g fill="none" stroke="var(--brand-blue)" stroke-width="2"><circle cx="12" cy="12" r="9"/><ellipse cx="12" cy="12" rx="4" ry="9"/><path d="M3 12h18M5 7h14M5 17h14"/></g></svg>
    <span>www.hdk-services.co.uk</span>
  </div>

  <div class="abs offer">
    <div class="offer__amount">%10</div>
    <div class="offer__label">Discount</div>
    <div class="offer__note">With this card</div>
  </div>
  <div class="abs offer-terms">Check our website for<br>full offer details</div>
</section>

<section class="card card--back" aria-label="Business card back">
  <svg class="card__art" viewBox="0 0 840 550" preserveAspectRatio="none" aria-hidden="true">
    <path d="M260 0 C 330 120, 300 300, 140 550 L 0 550 L 0 0 Z" fill="var(--card-shade)"/>
    <path d="M840 330 C 700 380, 560 470, 500 550 L 840 550 Z" fill="var(--card-shade)"/>
  </svg>

  <div class="trade-icons">
    <div class="trade-icon" style="background:#b07a45" role="img" aria-label="Carpentry trade icon"></div>
    <div class="trade-icon" style="background:#d9a41c" role="img" aria-label="Joinery trade icon"></div>
    <div class="trade-icon" style="background:#1787c9" role="img" aria-label="Water services trade icon"></div>
    <div class="trade-icon" style="background:#a3479a" role="img" aria-label="Bathroom fitting trade icon"></div>
    <div class="trade-icon" style="background:#1f86c6" role="img" aria-label="Building works trade icon"></div>
    <div class="trade-icon" style="background:#5f7482" role="img" aria-label="Drainage trade icon"></div>
    <div class="trade-icon" style="background:#f0d73c" role="img" aria-label="Maintenance trade icon"></div>
    <div class="trade-icon" style="background:#7d8a90" role="img" aria-label="Electrical trade icon"></div>
    <div class="trade-icon" style="background:#2fb1b8" role="img" aria-label="Appliance repair trade icon"></div>
    <div class="trade-icon" style="background:#1c8bd1" role="img" aria-label="Gas services trade icon"></div>
    <div class="trade-icon" style="background:#e03b3b" role="img" aria-label="Decorating trade icon"></div>
    <div class="trade-icon" style="background:#7fb541" role="img" aria-label="Pest control trade icon"></div>
  </div>

  <div class="abs headline">Your local all-trade experts</div>
  <div class="headline-rule"></div>
  <div class="abs field-label">Your HDK tradesman :</div>
  <div class="name-field"></div>

  <div class="abs feedback">
    <div class="feedback__question">What do you think of our service?</div>
    <div class="feedback__ask">Please leave feedback online</div>
    <div class="feedback__url">www.hdk-services.co.uk/feedback</div>
    <div class="feedback__stars">★★★★★★★★★★</div>
  </div>
</section>

</body>
</html>
```